Corporate Web Redesign Project - coded

We would like redesign/refresh of our current site that would allow us to increase the depth of content and create a high quality impression for visitors.

Current site - http://corvanisystems.com/

A previous web redesign project has improved our site but it has not really reached the level we require.

Our customers are global, blue chip, organisations and a professional, corporate style of site is required.

Please note we would prefer a coded website to a just a design. We are happy to provide a zip of our current site if required.
Updates

                                   

Target Market(s)

Global oil and gas producers, KR, Tamberline, Orvadex etc.

Industry/Entity Type

It Professional

Requirements
Must have
• Design should support the level of content we currently have in the existing sitemap - although it should be expandable a site design for a large / complex site would not be appropriate

All current content / pages to be reflected in design

Must be visually appealing

Intuitive and clear navigation that is expandable

Display a high level of professionalism

Use a consistent palette of colours that complements our logo

Clean and organized layout

A way to capture visitor’s information or Call to action (i.e. contact link or form) on every page

Prominent Contact Information
Should not have
• Flash

```html
<!DOCTYPE html>
<html lang="en">
<head>
<meta charset="utf-8">
<title>Corvani Systems – Optimize the Business of Drilling Wells</title>
<link rel="stylesheet" href="https://fonts.googleapis.com/css2?family=Arimo:wght@400;700&display=swap">
<style>
:root{
  --ink:#111;
  --white:#fff;
  --page:#e8e8e8;
  --teal:#3d7380;
  --teal-dark:#37636f;
  --aqua:#95c6c8;
  --aqua-light:#bcdcdc;
  --button-light:#a9d3d3;
  --black:#000;
  --nav-rule:#555;
  --client-grey:#9a9a9a;
  --sky-top:#4a7fb8;
  --sky-mid:#86acd2;
  --sea:#2a5888;
  --sea-deep:#1c416c;
}
*{box-sizing:border-box;margin:0;padding:0}
html,body{width:1010px;height:1200px;overflow:hidden}
body{position:relative;background:var(--page);font-family:"Arimo",Arial,sans-serif;color:var(--ink)}
a{color:inherit}
.abs{position:absolute}

/* hero */
.hero{left:0;top:0;width:1010px;height:476px;
  background:linear-gradient(180deg,var(--sky-top) 0%,var(--sky-mid) 60%,var(--sea) 80%,var(--sea-deep) 100%)}

.brand{left:124px;top:77px;width:189px;height:41px;background:var(--white);border:1px solid #333;
  display:flex;align-items:center;gap:8px;padding-left:12px;text-decoration:none}
.brand-mark{width:14px;height:14px;background:var(--teal)}
.brand-name{font-size:15px;font-weight:700;color:var(--teal-dark)}
.main-nav{left:313px;top:77px;width:546px;height:41px;background:var(--black);display:flex}
.main-nav a{color:var(--white);text-decoration:none;font-size:16px;display:flex;align-items:center;justify-content:center;border-right:1px solid var(--nav-rule);height:100%}
.main-nav a.nav-last-before{border-right:none}
.main-nav a:last-child{border:none;flex:1;justify-content:flex-end;padding-right:25px}

.hero-title{left:126px;top:183px;color:var(--white);font-size:23px;font-weight:700}
.hero-points{left:126px;top:218px;list-style:none;color:var(--white);font-size:19.5px;line-height:20px}
.hero-points li{display:flex;align-items:center;gap:5px}
.hero-cta{left:127px;top:296px;height:23px;display:flex;color:var(--white);font-size:14px;text-decoration:none}
.hero-cta span{background:var(--teal-dark);padding:3px 8px 0 8px}

/* service cards */
.card{top:420px;width:172px;height:158px;background:var(--white)}
.card-head{display:flex;gap:8px;padding:12px 0 0 16px;align-items:flex-start}
.card-title{color:var(--teal);font-weight:700;font-size:16px;line-height:16px}
.card-text{padding:16px 20px 0 25px;font-size:12.5px;line-height:12.5px}
.more{position:absolute;font-size:12.5px;display:flex;align-items:center;gap:3px}
.more::after{content:"";border-left:7px solid #222;border-top:4px solid transparent;border-bottom:4px solid transparent}

/* news & intro */
.news{left:126px;top:594px;width:172px;height:250px;background:var(--aqua-light)}
.news h2{font-size:13px;font-weight:700;text-align:center;margin-top:14px}
.news ul{list-style:none;margin:10px 0 0 16px}
.news li{font-size:11.5px;line-height:12px;display:flex;align-items:flex-start;gap:4px;margin-bottom:12px;width:140px}
.news li::before{content:"";flex:none;width:0;height:0;margin-top:2px;border-left:6px solid #222;border-top:4px solid transparent;border-bottom:4px solid transparent}
.intro{left:314px;top:594px;width:546px;height:250px;background:var(--aqua)}
.intro-col{position:absolute;top:14px;width:160px}
.intro-col h3{font-size:13px;font-weight:700;margin-bottom:6px;padding-left:4px}
.intro-photo{width:158px;height:72px;border:1px solid #555}
.intro-col p{font-size:12.5px;line-height:12.5px;margin-top:8px;width:150px;padding-left:4px}

/* clients */
.clients{left:126px;top:880px;width:734px;height:50px;display:flex;justify-content:space-between;align-items:center}
.client{color:var(--client-grey);font-size:17px;font-weight:700;display:flex;align-items:center;gap:5px}
.client i{width:12px;height:12px;background:var(--client-grey);display:block}

/* footer */
.footer{left:0;top:967px;width:1010px;height:233px;background:var(--black);color:var(--white)}
.enquiry h2{font-size:14.5px;font-weight:700;margin-bottom:7px}
.enquiry .field{width:195px;height:19px;background:var(--white);color:#222;font-size:11px;padding:3px 9px;margin-bottom:5px}
.enquiry .message{height:47px}
.submit{display:flex;font-size:13px;color:#222}
.submit span{background:var(--button-light);padding:2px 10px 0 12px}
.badge{width:156px;height:68px;background:#2a2a2a;border-radius:4px}
.follow{font-size:12.5px;font-weight:700}
.social{display:flex;gap:5px}
.social span{width:32px;height:32px;display:flex;align-items:center;justify-content:center;font-size:8px;color:var(--white)}
.office h3{font-size:13px;font-weight:700;margin-bottom:6px}
.office p{font-size:12.5px;line-height:12.5px}
.office .phone{margin-top:6px}
.office a{display:block;margin-top:3px;font-size:12.5px}
.legal{font-size:13px;text-align:right;line-height:19px}
</style>
</head>
<body>

<div class="abs hero" role="img" aria-label="Photograph of an orange semi-submersible drilling rig at sea under a blue sky"></div>

<a class="abs brand" href="http://corvanisystems.com/"><span class="brand-mark"></span><span class="brand-name">CORVANI SYSTEMS</span></a>
<nav class="abs main-nav">
  <a href="#" style="width:75px">News</a>
  <a href="#" style="width:78px">About</a>
  <a href="#" style="width:103px">Solutions</a>
  <a href="#" class="nav-last-before" style="width:108px">Newsroom</a>
  <a href="#">Contact Us</a>
</nav>

<h1 class="abs hero-title">Optimize the Business of Drilling Wells</h1>
<ul class="abs hero-points">
  <li><svg width="15" height="15" viewBox="0 0 16 16"><circle cx="8" cy="8" r="8" fill="#fff"/><path d="M4 8.3l2.7 2.7L12 5.5" stroke="#5b8ab8" stroke-width="2.2" fill="none"/></svg>Understanding projects costs &amp; risks</li>
  <li><svg width="15" height="15" viewBox="0 0 16 16"><circle cx="8" cy="8" r="8" fill="#fff"/><path d="M4 8.3l2.7 2.7L12 5.5" stroke="#5b8ab8" stroke-width="2.2" fill="none"/></svg>Control and reduce expenditure</li>
  <li><svg width="15" height="15" viewBox="0 0 16 16"><circle cx="8" cy="8" r="8" fill="#fff"/><path d="M4 8.3l2.7 2.7L12 5.5" stroke="#5b8ab8" stroke-width="2.2" fill="none"/></svg>Learn and improve performance</li>
</ul>
<a class="abs hero-cta" href="#"><span>Find out how</span><svg width="8" height="23" viewBox="0 0 8 23"><path d="M0 0L8 11.5 0 23z" fill="#37636f"/></svg></a>

<section class="abs card" style="left:126px">
  <div class="card-head"><svg width="30" height="30" viewBox="0 0 30 30"><circle cx="15" cy="15" r="15" fill="#3d7380"/><path d="M15 6v10h7" stroke="#fff" stroke-width="2.5" fill="none"/></svg><h2 class="card-title">Time &amp; Cost<br>Estimation</h2></div>
  <p class="card-text">TRK delivers a standardized, systematic approach to understanding project risk.</p>
  <a class="more" href="#" style="left:108px;top:135px">more</a>
</section>
<section class="abs card" style="left:313px">
  <div class="card-head"><svg width="22" height="30" viewBox="0 0 22 30"><rect width="22" height="30" rx="3" fill="#3d7380"/><rect x="4" y="4" width="14" height="6" fill="#fff"/><g fill="#fff"><rect x="4" y="13" width="3" height="3"/><rect x="9.5" y="13" width="3" height="3"/><rect x="15" y="13" width="3" height="3"/><rect x="4" y="18.5" width="3" height="3"/><rect x="9.5" y="18.5" width="3" height="3"/><rect x="15" y="18.5" width="3" height="3"/><rect x="4" y="24" width="3" height="3"/><rect x="9.5" y="24" width="3" height="3"/><rect x="15" y="24" width="3" height="3"/></g></svg><h2 class="card-title">Materials &amp;<br>Cost Control</h2></div>
  <p class="card-text" style="padding:16px 8px 0 19px">MCT has been helping companies optimize materials and cost tracking processes since 1992.</p>
  <a class="more" href="#" style="left:111px;top:135px">more</a>
</section>
<section class="abs card" style="left:500px">
  <div class="card-head"><svg width="40" height="30" viewBox="0 0 40 30"><path d="M20 4L40 12 20 20 0 12z" fill="#3d7380"/><path d="M9 16v8c6 4 16 4 22 0v-8l-11 5z" fill="#3d7380"/><path d="M4 13v10" stroke="#3d7380" stroke-width="2"/></svg><h2 class="card-title">Lessons<br>Learned</h2></div>
  <p class="card-text" style="padding:16px 24px 0 24px">LKX is an advanced lessons learned &amp; knowledge system for use in the energy industry.</p>
  <a class="more" href="#" style="left:110px;top:135px">more</a>
</section>
<section class="abs card" style="left:687px">
  <div class="card-head"><svg width="26" height="30" viewBox="0 0 26 30"><circle cx="13" cy="7" r="6.5" fill="#3d7380"/><path d="M0 30v-8c0-5 4-8 8-8h10c4 0 8 3 8 8v8z" fill="#3d7380"/><path d="M13 15l-2 5 2 8 2-8z" fill="#fff"/></svg><h2 class="card-title">Services &amp;<br>Consulting</h2></div>
  <p class="card-text" style="padding:16px 20px 0 23px">Successful software implementations rely on people and processes to deliver results.</p>
  <a class="more" href="#" style="left:108px;top:135px">more</a>
</section>

<section class="abs news">
  <h2>LATEST NEWS</h2>
  <ul>
    <li>TRK Selected by Westreach to provide probabilistic time and cost estimates for its drilling operations.</li>
    <li>MCT Implementation at Endora to support materials, logistics &amp; cost management processes.</li>
    <li>TRK Offset Data Mapper Assisting North Sea Estimates.</li>
  </ul>
  <a class="more" href="#" style="left:108px;top:211px">more</a>
</section>

<section class="abs intro">
  <div class="intro-col" style="left:14px">
    <h3>WHO WE ARE</h3>
    <div class="intro-photo" role="img" aria-label="Photograph of business people meeting by a bright window" style="background:linear-gradient(180deg,#dfe6ee,#8a96a6 70%,#2d323a)"></div>
    <p>An integrated software &amp; consulting organization with more than a decade of experiene, we help companies to understand, mitigate &amp; communicate risk &amp; control costs.</p>
  </div>
  <div class="intro-col" style="left:193px">
    <h3>WHAT WE DO</h3>
    <div class="intro-photo" role="img" aria-label="Photograph of a woman drawing a rising growth chart" style="background:linear-gradient(90deg,#e8d8c8,#f4f4f6 50%,#d8e4f0)"></div>
    <p>We deliver the tools, processes and people to facilitate major performance improvement and cost savings.</p>
  </div>
  <div class="intro-col" style="left:372px">
    <h3>HOW WE CAN HELP</h3>
    <div class="intro-photo" role="img" aria-label="Photograph of engineers reviewing plans on site" style="background:linear-gradient(90deg,#c9d6e2,#7d8c9c 60%,#3a4450)"></div>
    <p>Our solutions are used in more than 30 countries to support operations ranging from a single well to global deployments.</p>
  </div>
  <a class="more" href="#" style="left:79px;top:211px">contact us</a>
  <a class="more" href="#" style="left:263px;top:211px">learn more</a>
  <a class="more" href="#" style="left:447px;top:211px">get started</a>
</section>

<div class="abs clients">
  <span class="client"><i></i>Orvadex</span>
  <span class="client">Qarim</span>
  <span class="client">Aravon</span>
  <span class="client">Westreach</span>
  <span class="client"><i></i>KR</span>
  <span class="client">Endora</span>
  <span class="client">Halvik</span>
</div>

<footer class="abs footer">
  <form class="abs enquiry" style="left:126px;top:26px">
    <h2>Tell Us About Your Project</h2>
    <div class="field">your name</div>
    <div class="field">your email</div>
    <div class="field">company</div>
    <div class="field message">your nessage</div>
    <div class="submit" style="margin-left:126px;margin-top:9px"><span>submit</span><svg width="7" height="19" viewBox="0 0 7 19"><path d="M0 0L7 9.5 0 19z" fill="#a9d3d3"/></svg></div>
  </form>

  <div class="abs badge" style="left:364px;top:30px" role="img" aria-label="Software partner badge"></div>
  <div class="abs follow" style="left:368px;top:119px">follow us</div>
  <div class="abs social" style="left:367px;top:138px">
    <span style="background:#c8322a">Gathr</span>
    <span style="background:#2ea3dc">Chirp</span>
    <span style="background:#c0262a">Viewly</span>
    <span style="background:#3b5998">Friendo</span>
  </div>

  <address class="abs office" style="left:571px;top:34px;font-style:normal">
    <h3>EUROPE</h3>
    <p>18 Harlow Row<br>Kelmsford<br>KL4 2RD</p>
    <p class="phone">+44(0)1632 960418</p>
    <a href="#">eu@corvanisystems.com</a>
  </address>
  <address class="abs office" style="left:735px;top:34px;font-style:normal">
    <h3>NORTH AMERICA</h3>
    <p>1400 Ridgeline Pkwy<br>Suite 210<br>Marlow, TX 75001</p>
    <p class="phone">(555) 014 2278</p>
    <a href="#">us@corvanisystems.com</a>
  </address>

  <div class="abs legal" style="right:150px;top:162px">
    Privacy | Disclaimer | Terms | Privacy | Clients | Contact<br>
    Copyright © Corvani Systems Ltd 2013
  </div>
</footer>

</body>
</html>
```